Modern Poster Needed for Video Gaming Related Site

Pixelhavenspots.com is looking for a talented designer to create a unique, modern, and captivating poser capturing our brand/logo. Our website is dedicated to video gamers who are looking for unique video gaming locations (like a directory) scatter throughout america and creating an exclusive community for those who live the gamer life.
The overall design should include the attached logo somehow and with a tag line: "Find Your Game" somewhere in the design. For the style we would like to see a modern/simple but eye catching design. Lastly if possible a footer with our site address: www.pixelhavenspots.com with regard to text style we will leave this up to your imagination. Thank you for you consideration and checking out our project. Good luck to all of you and we look forward to seeing what extraordinary works you come up with.

```html
<!DOCTYPE html>
<html lang="en">
<head>
<meta charset="utf-8">
<title>Pixelhaven Spots – Find Your Game Poster</title>
<link rel="stylesheet" href="https://fonts.googleapis.com/css2?family=Anton&family=Montserrat:wght@700&display=swap">
<style>
  :root {
    --page-bg: #efefef;
    --poster-light: #ececec;
    --poster-mid: #d9d9d9;
    --studio-grey: #6f6f74;
    --studio-dark: #3b3a3e;
    --hair-brown: #4a2a22;
    --skin-warm: #c99a86;
    --skin-light: #dcc0b2;
    --controller-white: #d8dcdc;
    --band-black: #0a0a0a;
    --accent-orange: #e8502a;
    --accent-blue: #2855c9;
    --headline: #ffffff;
    --brand-ink: #1c1c1c;
    --logo-panel: #f3f3f3;
  }
  html, body {
    margin: 0;
    width: 1200px;
    height: 1148px;
    overflow: hidden;
    background: var(--page-bg);
  }
  .poster {
    position: absolute;
    left: 210px;
    top: 20px;
    width: 780px;
    height: 1108px;
    box-shadow: 0 6px 24px rgba(0,0,0,0.18);
  }
  .poster svg { display: block; }
  .headline {
    font-family: "Anton", "Impact", sans-serif;
    fill: var(--headline);
  }
  .brand-name {
    font-family: "Montserrat", "Arial", sans-serif;
    font-weight: 700;
    fill: var(--brand-ink);
    letter-spacing: 0.5px;
  }
  .site-address {
    font-family: "Montserrat", "Arial", sans-serif;
    font-weight: 700;
    fill: var(--accent-orange);
  }
</style>
</head>
<body>
  <div class="poster">
    <svg width="780" height="1108" viewBox="0 0 780 1108" xmlns="http://www.w3.org/2000/svg">
      <defs>
        <linearGradient id="poster-ground" x1="0" y1="0" x2="0" y2="1">
          <stop offset="0" stop-color="var(--poster-light)"/>
          <stop offset="1" stop-color="var(--poster-mid)"/>
        </linearGradient>
        <linearGradient id="photo-backdrop" x1="0" y1="0" x2="1" y2="0">
          <stop offset="0" stop-color="var(--studio-grey)"/>
          <stop offset="0.3" stop-color="var(--hair-brown)"/>
          <stop offset="0.7" stop-color="var(--hair-brown)"/>
          <stop offset="1" stop-color="var(--studio-dark)"/>
        </linearGradient>
        <radialGradient id="photo-warmth" cx="0.48" cy="0.4" r="0.42">
          <stop offset="0" stop-color="var(--skin-light)" stop-opacity="0.95"/>
          <stop offset="0.55" stop-color="var(--skin-warm)" stop-opacity="0.75"/>
          <stop offset="1" stop-color="var(--skin-warm)" stop-opacity="0"/>
        </radialGradient>
        <radialGradient id="photo-foreground" cx="0.55" cy="0.85" r="0.5">
          <stop offset="0" stop-color="var(--controller-white)" stop-opacity="0.8"/>
          <stop offset="1" stop-color="var(--controller-white)" stop-opacity="0"/>
        </radialGradient>
      </defs>

      <rect class="poster-ground" width="780" height="1108" fill="url(#poster-ground)"/>

      <g class="hero-photo" role="img"
         aria-label="Photo of a young woman with dark hair leaning in and gripping a game controller toward the viewer">
        <polygon points="0,0 780,0 780,454 0,643" fill="url(#photo-backdrop)"/>
        <polygon points="0,0 780,0 780,454 0,643" fill="url(#photo-warmth)"/>
        <polygon points="0,0 780,0 780,454 0,643" fill="url(#photo-foreground)"/>
      </g>

      <polygon class="band-edge-top" points="0,643 780,454 780,466 0,655" fill="var(--accent-orange)"/>
      <polygon class="tagline-band" points="0,655 780,466 780,676 0,875" fill="var(--band-black)"/>
      <polygon class="band-edge-bottom" points="0,875 780,676 780,690 0,889" fill="var(--accent-blue)"/>

      <text class="headline" x="390" y="712" font-size="128" text-anchor="middle"
            textLength="790" lengthAdjust="spacingAndGlyphs"
            transform="rotate(-13.6 390 668)">FIND YOUR GAME</text>

      <g class="brand-block">
        <rect class="logo-panel" x="335" y="800" width="360" height="218" fill="var(--logo-panel)"/>
        <rect class="brand-square" x="380" y="860" width="64" height="64" rx="8" fill="var(--accent-orange)"/>
        <text class="brand-name" x="458" y="887" font-size="28">PIXELHAVEN</text>
        <text class="brand-name" x="458" y="921" font-size="28">SPOTS</text>
        <text class="site-address" x="515" y="988" font-size="17" text-anchor="middle">www.pixelhavenspots.com</text>
      </g>
    </svg>
  </div>
</body>
</html>
```